Keelrock Data Partners (KDP) Business Card Design

I would like to create double-sided business cards that contain:
1) Name: Marcus Tolliver
2) Phone Number: +1 (555) 018-2947
3) Email: Marcus.Tolliver@KeelrockDataPartners.com
4) Website: KeelrockDataPartners.com

I would like to include my logo and a color scheme similar to the Vantorra Grand Prix Kelvex team color scheme (black, silver, greenish-blue – but can also include regular blue)

Logos attached.

What we do: Our company develops and delivers innovative and pragmatic information technology and cybersecurity risk and compliance solutions for organizations in the commercial market as well as the federal, and state/local sectors.

```html
<!DOCTYPE html>
<html lang="en">
<head>
<meta charset="utf-8">
<title>Keelrock Data Partners – Business Card</title>
<link href="https://fonts.googleapis.com/css2?family=Michroma&family=Roboto+Condensed:wght@700&family=Roboto:wght@400&display=swap" rel="stylesheet">
<style>
  :root {
    --stage: #3a3a3a;
    --card: #151515;
    --card-back: #101010;
    --edge: #2fd3cc;
    --teal: #3cc6c0;
    --blue: #1b6fc0;
    --silver: #d9d9d9;
    --rule: #6a6a6a;
    --tone-a: #0b0b0b;
    --tone-b: #262626;
  }
  * { margin: 0; padding: 0; box-sizing: border-box; }
  html, body { width: 1200px; height: 801px; overflow: hidden; }
  body {
    background: var(--stage);
    display: flex;
    align-items: center;
    justify-content: center;
    gap: 40px;
  }
  .card {
    position: relative;
    width: 540px;
    height: 309px;
    border-bottom: 3px solid var(--edge);
    border-left: 2px solid var(--edge);
    box-shadow: 0 10px 30px rgba(0,0,0,.45);
    overflow: hidden;
  }
  .card--front { background: var(--card); }
  .card--back { background: var(--card-back); }

  /* front */
  .brand {
    position: absolute;
    left: 58px;
    top: 48px;
    display: flex;
    align-items: center;
    gap: 18px;
  }
  .brand__mark {
    width: 64px; height: 64px;
    border-radius: 50%;
    background: var(--blue);
  }
  .brand__rule { width: 1px; height: 96px; background: var(--rule); }
  .brand__name {
    font-family: "Michroma", sans-serif;
    font-size: 24px;
    line-height: 1.05;
    color: var(--silver);
    text-transform: uppercase;
    letter-spacing: .5px;
  }
  .person {
    position: absolute;
    left: 58px;
    bottom: 44px;
    display: flex;
    align-items: center;
    gap: 20px;
  }
  .person__name {
    font-family: "Roboto Condensed", sans-serif;
    font-weight: 700;
    font-size: 24px;
    color: var(--teal);
    text-transform: uppercase;
    white-space: nowrap;
  }
  .person__rule { width: 1px; height: 62px; background: var(--rule); }
  .contact { list-style: none; font-family: "Roboto", sans-serif; font-size: 11.5px; color: var(--silver); }
  .contact li { display: flex; align-items: center; gap: 7px; line-height: 19px; }
  .contact svg { width: 10px; height: 10px; flex: none; }

  /* back */
  .back__pattern {
    position: absolute; inset: 0;
    background: linear-gradient(115deg, var(--tone-a) 0%, var(--tone-b) 55%, var(--tone-a) 100%);
  }
  .back__brand {
    position: absolute; left: 50%; top: 50%;
    transform: translate(-50%, -50%);
    display: flex; align-items: center; gap: 10px;
  }
  .back__mark { width: 22px; height: 22px; border-radius: 50%; background: var(--blue); }
  .back__name {
    font-family: "Michroma", sans-serif;
    font-size: 26px;
    color: var(--silver);
    letter-spacing: 1px;
  }
</style>
</head>
<body>
  <section class="card card--front" aria-label="Card front">
    <div class="brand">
      <span class="brand__mark" aria-hidden="true"></span>
      <span class="brand__rule"></span>
      <p class="brand__name">Keelrock<br>Data<br>Partners</p>
    </div>
    <div class="person">
      <p class="person__name">Marcus Tolliver</p>
      <span class="person__rule"></span>
      <ul class="contact">
        <li>
          <svg viewBox="0 0 10 10" aria-hidden="true"><path d="M2 1l2 2-1 1.2a6 6 0 0 0 2.8 2.8L7 6l2 2-1.3 1.3C4.5 9 1 5.5.7 2.3z" fill="#1b6fc0"/></svg>
          +1 (555) 018-2947
        </li>
        <li>
          <svg viewBox="0 0 10 10" aria-hidden="true"><rect x="0.5" y="2" width="9" height="6.5" fill="#1b6fc0"/><path d="M.5 2L5 5.5 9.5 2" stroke="#151515" fill="none"/></svg>
          Marcus.Tolliver@KeelrockDataPartners.com
        </li>
        <li>
          <svg viewBox="0 0 10 10" aria-hidden="true"><circle cx="5" cy="5" r="4.5" fill="#1b6fc0"/><path d="M.5 5h9M5 .5c-2 2.5-2 6.5 0 9M5 .5c2 2.5 2 6.5 0 9" stroke="#151515" stroke-width=".7" fill="none"/></svg>
          KeelrockDataPartners.com
        </li>
      </ul>
    </div>
  </section>

  <section class="card card--back" aria-label="Card back">
    <div class="back__pattern" role="img" aria-label="Tonal spot-gloss repeat pattern across the card back"></div>
    <div class="back__brand">
      <span class="back__mark" aria-hidden="true"></span>
      <span class="back__name">KDP</span>
    </div>
  </section>
</body>
</html>
```